Business Card Design

I am an independent chairman and director and work a lot in transformation/change and leadership environments. I work for both the New Zealand government and private companies in these capacities.
I've uploaded a basic graphic as a starting point - it is the Fibonacci sequence represented by the growth spiral. The numbers on the back of the card are the actual sequence.
As an idea the background could be gloss purple and the lettering raised print in bright silver.

Industry/Entity Type

Leadership

Contact Information for Business Card

Front
Dennis K. Harlow
Christchurch
New Zealand
dkharlow@quorvamail.co.nz

Mob.027.394.816
On ProLinkr

Back
Centered 1-1-2-3-5-8-13-21-34-55-89-144-233-377-610-987-1597

```html
<!DOCTYPE html>
<html lang="en">
<head>
<meta charset="utf-8">
<title>Dennis K. Harlow — Business Card</title>
<link rel="stylesheet" href="https://fonts.googleapis.com/css2?family=Fira+Sans:wght@400;600&display=swap">
<style>
  :root {
    --page-bg: #3a3d3b;
    --card-purple-light: #4f1a92;
    --card-purple: #41137c;
    --card-purple-dark: #2c0a58;
    --silver: #ffffff;
    --silver-soft: #e9e4f4;
    --shell-light: #b9b8f0;
    --shell-mid: #6f5fc4;
  }
  * { box-sizing: border-box; margin: 0; padding: 0; }
  html, body {
    width: 1200px;
    height: 1000px;
    overflow: hidden;
    background: var(--page-bg);
  }
  .business-card {
    position: absolute;
    left: 100px;
    top: 214px;
    width: 1000px;
    height: 572px;
    background: radial-gradient(ellipse at 35% 25%, var(--card-purple-light) 0%, var(--card-purple) 50%, var(--card-purple-dark) 100%);
    font-family: "Fira Sans", sans-serif;
    color: var(--silver);
  }
  .growth-spiral {
    position: absolute;
    left: 520px;
    top: 120px;
    width: 190px;
    height: 190px;
    border-radius: 50%;
    background: radial-gradient(circle at 55% 55%, var(--shell-light) 0%, var(--shell-mid) 45%, rgba(111, 95, 196, 0) 72%);
    opacity: 0.75;
  }
  .contact-block {
    position: absolute;
    left: 72px;
    top: 366px;
    line-height: 1.45;
  }
  .contact-line {
    font-size: 29px;
    font-weight: 400;
    color: var(--silver-soft);
    white-space: nowrap;
  }
  .holder-name {
    font-weight: 600;
    color: var(--silver);
  }
  .divider { padding: 0 6px; }
</style>
</head>
<body>
  <div class="business-card">
    <div class="growth-spiral" role="img" aria-label="Nautilus shell growth spiral illustration in pale silver-violet lines"></div>
    <div class="contact-block">
      <p class="contact-line"><span class="holder-name">Dennis K. Harlow</span><span class="divider">|</span>Christchurch<span class="divider">|</span>New Zealand</p>
      <p class="contact-line">dkharlow@quorvamail.co.nz<span class="divider">|</span>Mob.027.394.816<span class="divider">|</span>On ProLinkr</p>
    </div>
  </div>
</body>
</html>
```